Graphic to communicate emotional connection

Howdy-I need a graphic that describe my financial planning process.The attached is a concept, but please use your own creativity to show how you would display this:- The four circles on the outside (Protect what we have, know where it goes, make it grow, and dignity and independence) are the four major areas of concern- Then, there are three value statements:- The first is the most powerful which is that Clarity leads to Control which allows your Intentions to come through- The second shows that we take our clients from Uncertainty and Confusion, to Confidence and Intention- The third says we create space for you to develop your Purposeful Effort which leads to Your Best Financial Life.I've also attached my logo - please use the colors in my logo and maybe add a soft green as needed.The reader should be able to briefly scan this document and understand that we will connect with them on an emotional level to get their finances in shape.Thanks!-Ned

Target Market(s)

wealthy women, whether independent or married

Industry/Entity Type

Financial Planning

Requirements
Must have
• Please use the colors in my logo plus a soft green as needed
Should not have
• This should not be a busy or hard-to-read graphic. It is meant to convey an that I try to make an emotional connection, at a glance.

```html
<!DOCTYPE html>
<html lang="en">
<head>
<meta charset="utf-8">
<title>Our Aspiration – Harbor Wealth Management</title>
<link href="https://fonts.googleapis.com/css2?family=Tinos:wght@400&display=swap" rel="stylesheet">
<style>
:root{
  --page:#d5e1ef;
  --navy:#0f3a80;
  --navy-deep:#0b2f6b;
  --grey:#676767;
  --grey-deep:#575757;
  --green-soft:#d6ecce;
  --steel:#a3b5d3;
  --white:#ffffff;
  --label:#4a4a4a;
}
*{box-sizing:border-box;margin:0;padding:0}
html,body{width:979px;height:1200px;overflow:hidden}
body{background:var(--page);font-family:"Tinos","Times New Roman",serif;position:relative}
.frame{position:absolute;left:52px;top:62px;width:875px;height:1078px;border:2px solid var(--navy-deep);background:var(--white)}
.panel{position:absolute;left:0;width:871px;overflow:hidden}
.panel--first{top:0;height:548px;border-bottom:2px solid var(--navy-deep)}
.panel--second{top:548px;height:526px}
.panel__inner{position:absolute;left:-52px;top:-62px;width:979px;height:620px}
.panel--second .panel__inner{top:-60px}

.brand{position:absolute;left:398px;top:92px;display:flex;align-items:center;gap:8px;color:var(--navy)}
.brand__mark{width:34px;height:34px;background:var(--navy)}
.brand__name{font-size:17px;line-height:1.05;letter-spacing:.3px}
.brand__name small{display:block;font-size:10px;letter-spacing:.6px}

.title{position:absolute;left:0;width:979px;top:152px;text-align:center;font-size:31px;color:var(--navy);letter-spacing:.5px;font-weight:400}
.title__rule{position:absolute;left:355px;width:251px;top:189px;height:2px;background:linear-gradient(90deg,transparent,var(--navy) 8%,var(--navy) 92%,transparent)}
.panel--second .title__rule{left:320px;width:330px;background:linear-gradient(90deg,transparent,#333 20%,#333 80%,transparent);height:1.5px}

.concern{position:absolute;width:125px;height:88px;border-radius:10px;color:var(--white);display:flex;align-items:center;justify-content:center;text-align:center;font-size:17px;line-height:19px;overflow:hidden;text-transform:uppercase}
.concern::before{content:"";position:absolute;left:-40px;top:-95px;width:240px;height:140px;border-radius:50%;background:rgba(255,255,255,.14)}
.concern span{position:relative}
.concern--navy{background:linear-gradient(160deg,#1b4c98,var(--navy-deep))}
.concern--grey{background:linear-gradient(160deg,#777,var(--grey-deep))}
.concern--small{font-size:14px;line-height:16px}
.pos-tl{left:122px;top:223px}
.pos-tr{left:722px;top:223px}
.pos-bl{left:122px;top:469px}
.pos-br{left:722px;top:469px}

.flow{position:absolute;left:272px;top:234px;width:424px;height:77px}
.flow__shape{position:absolute;left:0;top:0;width:424px;height:77px}
.flow__step{position:absolute;top:26px;font-size:21px;line-height:26px;color:var(--navy);white-space:nowrap}
.flow__chev{position:absolute;top:30px;width:23px;height:19px}
.step-1{left:13px}
.chev-1{left:111px}
.step-2{left:145px}
.chev-2{left:249px}
.step-3{left:279px}

.stage{position:absolute;width:154px;height:50px}
.stage__pill{position:absolute;inset:3px;border-radius:25px;color:var(--white);display:flex;align-items:center;justify-content:center;text-align:center;font-size:13px;line-height:15px;letter-spacing:.2px}
.stage::before{content:"";position:absolute;inset:-2px;border-radius:28px;border:2px solid var(--navy);border-top-color:transparent;border-bottom-color:transparent}
.stage__label{position:absolute;left:-20px;right:-20px;top:-13px;text-align:center;font-size:8.5px;line-height:9.5px;color:var(--label);text-transform:uppercase;letter-spacing:.2px}
.stage__label--two{top:-23px}
.panel--first .stage__pill{background:var(--grey)}
.panel--second .stage__pill{background:var(--navy)}
.s-a{left:272px;top:364px}
.s-b{left:546px;top:364px}
.s-c{left:272px;top:438px}
.s-d{left:546px;top:438px}
.step-arrow{position:absolute;left:462px;width:42px;height:38px}
.step-arrow--one{top:370px}
.step-arrow--two{top:444px}
</style>
</head>
<body>
<div class="frame">

  <section class="panel panel--first">
    <div class="panel__inner">
      <div class="brand"><div class="brand__mark"></div><div class="brand__name">HARBOR WEALTH<small>MANAGEMENT, LLC</small></div></div>
      <h1 class="title">OUR ASPIRATION</h1>
      <div class="title__rule"></div>

      <div class="concern concern--navy pos-tl"><span>Protect<br>what we<br>have</span></div>
      <div class="concern concern--navy pos-tr"><span>Know<br>where it<br>goes</span></div>
      <div class="concern concern--navy pos-bl"><span>Make it<br>grow</span></div>
      <div class="concern concern--navy concern--small pos-br"><span>Dignity and<br>independence</span></div>

      <div class="flow">
        <svg class="flow__shape" viewBox="0 0 424 77" preserveAspectRatio="none"><path d="M0 20H372V0L424 38.5 372 77V57H0Z" fill="var(--green-soft)"/></svg>
        <span class="flow__step step-1">CLARITY</span>
        <svg class="flow__chev chev-1" viewBox="0 0 24 20"><path d="M0 6H12V0L24 10 12 20V14H0Z" fill="#fff"/></svg>
        <span class="flow__step step-2">CONTROL</span>
        <svg class="flow__chev chev-2" viewBox="0 0 24 20"><path d="M0 6H12V0L24 10 12 20V14H0Z" fill="#fff"/></svg>
        <span class="flow__step step-3">INTENTION</span>
      </div>

      <div class="stage s-a"><div class="stage__label">We take you from</div><div class="stage__pill">UNCERTAINTY<br>CONFUSION</div></div>
      <svg class="step-arrow step-arrow--one" viewBox="0 0 42 38"><path d="M0 11H22V0L42 19 22 38V27H0Z" fill="var(--steel)"/></svg>
      <div class="stage s-b"><div class="stage__label">To</div><div class="stage__pill">CONFIDENCE<br>INTENTION</div></div>

      <div class="stage s-c"><div class="stage__label stage__label--two">We create space<br>for your</div><div class="stage__pill">PURPOSEFUL<br>EFFORT</div></div>
      <svg class="step-arrow step-arrow--two" viewBox="0 0 42 38"><path d="M0 11H22V0L42 19 22 38V27H0Z" fill="var(--steel)"/></svg>
      <div class="stage s-d"><div class="stage__label">Witch leads to</div><div class="stage__pill">YOUR BEST<br>FINANCIAL LIFE</div></div>
    </div>
  </section>

  <section class="panel panel--second">
    <div class="panel__inner">
      <div class="brand"><div class="brand__mark"></div><div class="brand__name">HARBOR WEALTH<small>MANAGEMENT, LLC</small></div></div>
      <h2 class="title">OUR ASPIRATION</h2>
      <div class="title__rule"></div>

      <div class="concern concern--grey pos-tl"><span>Protect<br>what we<br>have</span></div>
      <div class="concern concern--grey pos-tr"><span>Know<br>where it<br>goes</span></div>
      <div class="concern concern--grey pos-bl"><span>Make it<br>grow</span></div>
      <div class="concern concern--grey concern--small pos-br"><span>Dignity and<br>independence</span></div>

      <div class="flow">
        <svg class="flow__shape" viewBox="0 0 424 77" preserveAspectRatio="none"><path d="M0 20H372V0L424 38.5 372 77V57H0Z" fill="var(--steel)"/></svg>
        <span class="flow__step step-1">CLARITY</span>
        <svg class="flow__chev chev-1" viewBox="0 0 24 20"><path d="M0 6H12V0L24 10 12 20V14H0Z" fill="#fff"/></svg>
        <span class="flow__step step-2">CONTROL</span>
        <svg class="flow__chev chev-2" viewBox="0 0 24 20"><path d="M0 6H12V0L24 10 12 20V14H0Z" fill="#fff"/></svg>
        <span class="flow__step step-3">INTENTION</span>
      </div>

      <div class="stage s-a"><div class="stage__label">We take you from</div><div class="stage__pill">UNCERTAINTY<br>CONFUSION</div></div>
      <svg class="step-arrow step-arrow--one" viewBox="0 0 42 38"><path d="M0 11H22V0L42 19 22 38V27H0Z" fill="var(--steel)"/></svg>
      <div class="stage s-b"><div class="stage__label">To</div><div class="stage__pill">CONFIDENCE<br>INTENTION</div></div>

      <div class="stage s-c"><div class="stage__label stage__label--two">We create space<br>for your</div><div class="stage__pill">PURPOSEFUL<br>EFFORT</div></div>
      <svg class="step-arrow step-arrow--two" viewBox="0 0 42 38"><path d="M0 11H22V0L42 19 22 38V27H0Z" fill="var(--steel)"/></svg>
      <div class="stage s-d"><div class="stage__label">Witch leads to</div><div class="stage__pill">YOUR BEST<br>FINANCIAL LIFE</div></div>
    </div>
  </section>

</div>
</body>
</html>
```